Canadian Christian Church needs design for new sermon series

A graphic design for our series and an invitation card to invite people to the series. Check design brief for more detailed information. Target audience: young families and young adults. Looking for a creative design that will get people's attention and create interest. See design brief for copy of design purchased for previous series.
Updates
entered Apr 4 incorrectly. Need a week to receive and review designs, and today is Apr 2/19. Thanks!
Target Market(s)
young families and young adults
Colors
Designer to choose colors to be used in the design.
Look and feel

```html
<!DOCTYPE html>
<html lang="en">
<head>
<meta charset="utf-8">
<title>Messy – Sermon Series Invitation</title>
<link rel="stylesheet" href="https://fonts.googleapis.com/css2?family=Merriweather:wght@700;900&family=Source+Sans+3:wght@400;600;700&family=Comfortaa:wght@400;500&family=Tinos&display=swap">
<style>
  :root {
    --page-bg: #ebe6e0;
    --card-front-dark: #4e3a47;
    --card-front-light: #6b5561;
    --card-back-dark: #6a5460;
    --card-back-light: #8c7680;
    --band: #3f2d3b;
    --ink: #ffffff;
    --ink-soft: #f1eaee;
    --rule: #e9e1e5;
    --logo-dot: #c98a3a;
    --title-light: #e4e0e2;
    --title-mid: #cdc6ca;
  }
  * { box-sizing: border-box; margin: 0; padding: 0; }
  html, body { width: 1200px; height: 1200px; overflow: hidden; }
  body { background: var(--page-bg); position: relative; }

  .card {
    position: absolute;
    left: 250px;
    width: 668px;
    height: 524px;
    overflow: hidden;
    box-shadow: 0 6px 18px rgba(40, 25, 35, 0.28);
    color: var(--ink);
  }
  .card--front {
    top: 44px;
    background: radial-gradient(ellipse at 45% 40%, var(--card-front-light) 0%, var(--card-front-dark) 75%);
  }
  .card--back {
    top: 616px;
    background: radial-gradient(ellipse at 40% 45%, var(--card-back-light) 0%, var(--card-back-dark) 80%);
  }

  .church-mark {
    position: absolute;
    display: flex;
    flex-direction: column;
    align-items: center;
    font-family: 'Tinos', serif;
    color: var(--ink-soft);
    white-space: nowrap;
  }
  .church-mark__dot { border-radius: 50%; background: var(--logo-dot); }
  .church-mark--front { left: 430px; top: 40px; width: 220px; font-size: 15px; }
  .church-mark--front .church-mark__dot { width: 62px; height: 62px; margin-bottom: 10px; }
  .church-mark--back { left: 413px; top: 348px; width: 180px; font-size: 12px; }
  .church-mark--back .church-mark__dot { width: 48px; height: 48px; margin-bottom: 6px; }

  .series-title-art {
    position: absolute;
    left: 82px;
    top: 158px;
    width: 504px;
    height: 190px;
    border-radius: 6px;
    background: linear-gradient(135deg, var(--title-light) 0%, var(--title-mid) 100%);
    opacity: 0.85;
    box-shadow: 3px 4px 8px rgba(20, 10, 18, 0.35);
  }

  .tagline-band {
    position: absolute;
    left: 0; right: 0;
    top: 418px;
    height: 86px;
    background: var(--band);
    display: flex;
    align-items: center;
    justify-content: center;
    font-family: 'Merriweather', serif;
    font-weight: 900;
    font-size: 43px;
    color: var(--ink);
  }

  .invite {
    position: absolute;
    left: 0; right: 0;
    top: 22px;
    text-align: center;
    font-family: 'Source Sans 3', sans-serif;
    font-weight: 700;
    line-height: 1.1;
  }
  .invite__lead { font-size: 32px; }
  .invite__time { font-size: 43px; }

  .column { position: absolute; top: 136px; width: 236px; }
  .column--dates { left: 46px; }
  .column--features { left: 386px; }
  .column__heading {
    border-top: 2px solid var(--rule);
    border-bottom: 2px solid var(--rule);
    height: 58px;
    display: flex;
    align-items: center;
    justify-content: center;
    font-family: 'Source Sans 3', sans-serif;
    font-weight: 700;
    font-size: 23px;
  }

  .list {
    list-style: none;
    position: absolute;
    font-family: 'Comfortaa', sans-serif;
    font-size: 14.5px;
    color: var(--ink-soft);
  }
  .list li { height: 25.2px; display: flex; align-items: center; white-space: nowrap; }
  .list li::before { content: "\2020"; font-family: 'Source Sans 3', sans-serif; font-weight: 700; width: 18px; }
  .list--dates { left: 41px; top: 218px; }
  .list--dates .date { display: inline-block; width: 80px; }
  .list--features { left: 422px; top: 218px; }

  .contact-band {
    position: absolute;
    left: 0; right: 0; bottom: 0;
    height: 72px;
    background: var(--band);
    display: flex;
    flex-direction: column;
    align-items: center;
    justify-content: center;
    gap: 4px;
    font-family: 'Source Sans 3', sans-serif;
    font-weight: 600;
    font-size: 14px;
    color: var(--ink);
  }
</style>
</head>
<body>

<section class="card card--front">
  <div class="church-mark church-mark--front">
    <span class="church-mark__dot"></span>
    <span class="church-mark__name">Maple Hollow Community Church</span>
  </div>
  <div class="series-title-art" role="img" aria-label="Series title artwork: the word Messy in large white torn, shredded lettering"></div>
  <div class="tagline-band">Joining God in the Mess</div>
</section>

<section class="card card--back">
  <div class="invite">
    <p class="invite__lead">Join Us,</p>
    <p class="invite__time">Sundays @ 10:30</p>
  </div>

  <div class="column column--dates"><h2 class="column__heading">Dates &amp; Topics</h2></div>
  <div class="column column--features"><h2 class="column__heading">Featuring</h2></div>

  <ul class="list list--dates">
    <li><span class="date">April 28th</span>: “We Made This Mess”</li>
    <li><span class="date">May 5th</span>: “Bless in the Mess”</li>
    <li><span class="date">May 12th</span>: “Born into the Mess”</li>
    <li><span class="date">May 19th</span>: “Messy Work”</li>
    <li><span class="date">May 26th</span>: “Messy Church”</li>
    <li><span class="date">June 2nd</span>: “Messy Hospitality”</li>
    <li><span class="date">June 9th</span>: TBD</li>
    <li><span class="date">June 16th</span>: “Messy within Boundaries”</li>
  </ul>

  <ul class="list list--features">
    <li>Staffed nursery</li>
    <li>Children’s program</li>
    <li>Coffee &amp; snacks</li>
    <li>Everyone welcome</li>
  </ul>

  <div class="church-mark church-mark--back">
    <span class="church-mark__dot"></span>
    <span class="church-mark__name">Maple Hollow Community Church</span>
  </div>

  <footer class="contact-band">
    <p>Location – 1875 Cedar Ridge Road, Oakmont, ON L9T 4B2</p>
    <p>Phone – 555.014.2718 | Email-hello@maplehollowchurch.ca | Website-www.maplehollowchurch.ca</p>
  </footer>
</section>

</body>
</html>
```